Financial Services Postcard Design

Lionel Budwig, CPA
Financial Services
Accounting/Tax/Consulting
Services include but not limited to
Financial Statements
Tax Returns
CFO/Controller services
Budgeting and Forecasting
Cash Management
Payroll / AP/ AR
Insurance Analysis
Cost Analysis
Special projects

I need a postcard design for my new financial service company to assist businesses in the Orange County area of southern California. I'm looking for a warm but bright look to represent CPA with many years of Management experience with manufacturing companies that can relate to business issues and provide solutions for small business.

```html
<!DOCTYPE html>
<html lang="en">
<head>
<meta charset="utf-8">
<title>Lionel Budwig, CPA – Postcard</title>
<link rel="stylesheet" href="https://fonts.googleapis.com/css2?family=Cinzel:wght@500;600&family=Crimson+Pro:wght@400;500&display=swap">
<style>
  :root {
    --backdrop: #5a5a5a;
    --navy: #1b3863;
    --navy-deep: #132a4d;
    --gold: #e3a31a;
    --gold-light: #f0b93a;
    --gold-dark: #b57d0c;
    --paper: #ffffff;
    --ink: #1e2f4f;
    --photo-tone: #c9c2bb;
    --portrait-tone: #b8aca3;
  }
  * { margin: 0; padding: 0; box-sizing: border-box; }
  html, body { width: 907px; height: 1200px; overflow: hidden; }
  body { background: var(--backdrop); position: relative; font-family: "Crimson Pro", Georgia, serif; }

  .card { position: absolute; overflow: hidden; box-shadow: 0 4px 14px rgba(0,0,0,.45); }
  .card-front { left: 80px; top: 44px; width: 750px; height: 538px; background: var(--navy); }
  .card-back { left: 80px; top: 615px; width: 756px; height: 543px; background: var(--paper); }
  .card svg.shapes { position: absolute; left: 0; top: 0; }

  .headline-box { position: absolute; left: 0; top: 96px; width: 352px; height: 278px; text-align: center;
    background: linear-gradient(135deg, var(--gold-light), var(--gold) 55%, var(--gold-dark)); }
  .firm-name { font-family: "Cinzel", serif; font-weight: 600; font-size: 29px; color: var(--ink); margin-top: 36px; letter-spacing: .5px; }
  .firm-tag { font-size: 16px; letter-spacing: 1.4px; color: var(--ink); padding: 4px 0 6px; margin: 0 44px;
    border-bottom: 1px solid rgba(30,47,79,.5); }
  .headline { color: var(--paper); line-height: .95; margin-top: 22px; text-shadow: 0 2px 3px rgba(0,0,0,.25); }
  .headline .l1 { display: block; font-size: 47px; }
  .headline .l2 { display: block; font-size: 54px; }
  .headline-sub { font-size: 20px; font-weight: 500; color: var(--ink); margin-top: 12px; }

  .about-tab { position: absolute; left: 123px; top: 17px; width: 200px; height: 65px;
    background: linear-gradient(180deg, var(--gold-light), var(--gold)); font-family: "Cinzel", serif; font-weight: 600;
    font-size: 36px; color: var(--ink); text-align: center; line-height: 67px; box-shadow: 0 2px 4px rgba(0,0,0,.3); }
  .about-copy { position: absolute; left: 21px; top: 102px; width: 405px; color: #fff; font-size: 14.2px; line-height: 16px; }
  .about-copy p + p { margin-top: 16px; }
  .service-list { position: absolute; top: 216px; list-style: none; color: #fff; font-size: 14.5px; line-height: 20.8px; }
  .service-list.col-a { left: 34px; }
  .service-list.col-b { left: 248px; }
  .service-list li { padding-left: 15px; position: relative; }
  .service-list li::before { content: ""; position: absolute; left: 0; top: 7px; width: 7px; height: 7px; border-radius: 50%; background: var(--gold); }

  .contact { position: absolute; left: 33px; top: 405px; color: var(--ink); font-size: 13.5px; line-height: 16px; }
  .contact-name { font-size: 20px; color: var(--gold-dark); margin: 0 0 3px 16px; }
  .contact-row { display: flex; gap: 6px; margin-bottom: 9px; }
  .contact-row svg { flex: none; margin-top: 2px; }

  .stamp-box { position: absolute; left: 657px; top: 67px; width: 58px; height: 73px; border: 1.5px solid #222; }
  .address-line { position: absolute; left: 494px; width: 227px; border-top: 1.5px solid #222; }
</style>
</head>
<body>

<section class="card card-front">
  <svg class="shapes" width="750" height="538" viewBox="0 0 750 538">
    <defs>
      <linearGradient id="navyFade" x1="0" y1="0" x2="1" y2="1">
        <stop offset="0" stop-color="#23457a"/><stop offset="1" stop-color="#132a4d"/>
      </linearGradient>
      <linearGradient id="goldBand" x1="0" y1="0" x2="1" y2="0">
        <stop offset="0" stop-color="#f0b93a"/><stop offset="1" stop-color="#d9960f"/>
      </linearGradient>
      <linearGradient id="photoTone" x1="0" y1="0" x2="1" y2="1">
        <stop offset="0" stop-color="#ece8e2"/><stop offset="1" stop-color="#a79c93"/>
      </linearGradient>
    </defs>
    <rect width="750" height="538" fill="url(#navyFade)"/>
    <polygon points="320,74 750,0 750,488 320,398" fill="url(#photoTone)" role="img" aria-label="Photo of a team of four office professionals reviewing work at a computer"/>
    <polygon points="320,74 352,76 352,96 320,96" fill="#9a6a08"/>
    <polygon points="0,410 750,525 750,538 0,538" fill="url(#goldBand)"/>
    <polygon points="0,478 700,538 0,538" fill="#ffffff"/>
  </svg>
  <div class="headline-box">
    <div class="firm-name">Lionel Budwig, CPA</div>
    <div class="firm-tag">FINANCIAL SERVICE COMPANY</div>
    <h1 class="headline"><span class="l1">Management</span><span class="l2">Experience</span></h1>
    <div class="headline-sub">with manufacturing companies</div>
  </div>
</section>

<section class="card card-back">
  <svg class="shapes" width="756" height="543" viewBox="0 0 756 543">
    <defs>
      <linearGradient id="panelFade" x1="0" y1="0" x2="1" y2="1">
        <stop offset="0" stop-color="#132a4d"/><stop offset="1" stop-color="#23457a"/>
      </linearGradient>
      <linearGradient id="bandGold" x1="0" y1="0" x2="1" y2="0">
        <stop offset="0" stop-color="#f0b93a"/><stop offset="1" stop-color="#d9960f"/>
      </linearGradient>
    </defs>
    <rect x="0" y="45" width="442" height="355" fill="url(#panelFade)"/>
    <polygon points="0,323 442,392 442,420 0,382" fill="url(#bandGold)"/>
    <polygon points="0,374 442,445 442,543 0,543" fill="#ffffff"/>
    <polygon points="113,17 123,17 123,45" fill="#9a6a08"/>
    <polygon points="333,17 323,17 323,45" fill="#9a6a08"/>
    <circle cx="353" cy="432" r="96" fill="#e3a31a"/>
    <circle cx="353" cy="432" r="88" fill="#b8aca3" role="img" aria-label="Portrait photo of the accountant in a dark suit"/>
  </svg>

  <div class="about-tab">About Us</div>
  <div class="about-copy">
    <p>We are a new financial service company to assist businesses in the Orange County area of southern California. We have many years of Management experience with manufacturing companies that can relate to business issues and provide solutions for small business.</p>
    <p>Services include but not limited to:</p>
  </div>
  <ul class="service-list col-a">
    <li>Financial Statements</li><li>Tax Returns</li><li>CFO/Controller services</li><li>Budgeting and Forecasting</li><li>Accounting/Tax/Consulting</li>
  </ul>
  <ul class="service-list col-b">
    <li>Cash Management</li><li>Payroll / AP/ AR</li><li>Insurance Analysis</li><li>Cost Analysis</li><li>Special projects</li>
  </ul>

  <div class="contact">
    <div class="contact-name">Lionel Budwig, CPA</div>
    <div class="contact-row">
      <svg width="9" height="12" viewBox="0 0 9 12"><path d="M4.5 0A4.5 4.5 0 0 0 0 4.5C0 8 4.5 12 4.5 12S9 8 9 4.5A4.5 4.5 0 0 0 4.5 0zm0 6.3a1.8 1.8 0 1 1 0-3.6 1.8 1.8 0 0 1 0 3.6z" fill="#e3a31a"/></svg>
      <span>118 N Larkspur Ln.<br>Anaheim Hills, Ca. 92800</span>
    </div>
    <div class="contact-row">
      <svg width="10" height="12" viewBox="0 0 10 12"><path d="M2 0l2 3-1.2 1.2c.6 1.6 1.6 2.8 3.2 3.6L7.2 6.6 10 8.6 8.8 11C4 11 0 6 0 1.2z" fill="#e3a31a"/></svg>
      <span>714-555-0142</span>
    </div>
    <div class="contact-row">
      <svg width="11" height="9" viewBox="0 0 11 9" style="margin-top:4px"><rect width="11" height="8" fill="#e3a31a"/><path d="M0 0l5.5 4.5L11 0" fill="none" stroke="#fff" stroke-width="1"/></svg>
      <span>LBudwig@ledgerpost.net</span>
    </div>
  </div>

  <div class="stamp-box"></div>
  <div class="address-line" style="top:297px"></div>
  <div class="address-line" style="top:337px"></div>
  <div class="address-line" style="top:377px"></div>
</section>

</body>
</html>
```